VFX Company Business Card Design Project

The Ember Vale is a decentralized Visual Effects Studio servicing the television and feature film industries.
Project Brief:
Take our logo that was previously designed on Pixel Harbor and make a double sided business card.
Requirements:
- Card MUST be double sided.
- Front of card MUST have the yellow part of our logo against the dark grey background.
- Back of card is completely up to the designer.
- Back of card must include the complete company logo.
Please follow these File Preparation guidelines:
http://printmoor.example/infopage?file=filetype_en&s=PrintMoor_new&lang=en
Industry/Entity Type
Business
Look and feel
Each slider illustrates characteristics of the customer's brand and the style your logo design should communicate.

```html
<!DOCTYPE html>
<html lang="en">
<head>
<meta charset="utf-8">
<title>The Ember Vale – Business Card</title>
<link rel="stylesheet" href="https://fonts.googleapis.com/css2?family=Quicksand:wght@400;500;600&display=swap">
<style>
  :root {
    --backdrop: #3b3e3d;
    --card-dark: #2f3031;
    --card-dark-edge: #3a3b3c;
    --card-light: #f4f4f2;
    --accent: #e7bd22;
    --brand-grey: #9aa3a6;
    --text-dark: #2b2c2d;
    --text-muted: #55585a;
  }
  * { box-sizing: border-box; margin: 0; padding: 0; }
  html, body { width: 1200px; height: 900px; overflow: hidden; }
  body {
    background: var(--backdrop);
    font-family: "Quicksand", sans-serif;
    position: relative;
  }
  .card {
    position: absolute;
    top: 300px;
    width: 520px;
    height: 300px;
    border-radius: 3px;
    overflow: hidden;
    box-shadow: 0 14px 30px rgba(0,0,0,0.35);
  }
  .card-front {
    left: 60px;
    background: linear-gradient(160deg, var(--card-dark-edge), var(--card-dark));
    display: flex;
    align-items: center;
    justify-content: center;
  }
  .card-back { left: 620px; background: var(--card-light); }

  .brand { display: flex; align-items: center; gap: 14px; }
  .brand-dot {
    width: 38px; height: 38px; border-radius: 50%;
    background: var(--accent);
  }
  .brand-name {
    font-weight: 600;
    font-size: 34px;
    letter-spacing: 1px;
    color: var(--brand-grey);
    text-transform: uppercase;
  }
  .card-back .brand {
    position: absolute; left: 34px; top: 34px; gap: 10px;
  }
  .card-back .brand-dot { width: 24px; height: 24px; }
  .card-back .brand-name { font-size: 21px; }

  .back-bands { position: absolute; inset: 0; }

  .holder {
    position: absolute; right: 20px; top: 112px;
    text-align: right; color: var(--text-dark);
  }
  .holder-name { font-size: 17px; font-weight: 500; letter-spacing: 1px; text-transform: uppercase; }
  .holder-role { font-size: 10px; color: var(--text-muted); margin-top: 1px; }

  .contact-list {
    position: absolute; left: 290px; top: 186px;
    list-style: none;
  }
  .contact-list li {
    display: flex; align-items: center; gap: 12px;
    font-size: 12.5px; color: var(--text-dark);
    height: 20px;
  }
  .contact-list .web-accent { color: var(--accent); }
  .icon {
    width: 13px; height: 13px; border-radius: 50%;
    background: var(--text-dark);
    display: flex; align-items: center; justify-content: center;
    flex: none;
  }
  .address {
    position: absolute; left: 26px; top: 236px;
    display: flex; gap: 10px; align-items: flex-start;
    font-size: 12.5px; line-height: 1.35; color: var(--text-dark);
  }
  .address .icon { background: var(--accent); margin-top: 4px; }
</style>
</head>
<body>

  <section class="card card-front" aria-label="Card front">
    <div class="brand">
      <span class="brand-dot"></span>
      <span class="brand-name">The Ember Vale</span>
    </div>
  </section>

  <section class="card card-back" aria-label="Card back">
    <svg class="back-bands" width="520" height="300" viewBox="0 0 520 300" aria-hidden="true">
      <rect x="0" y="0" width="520" height="102" fill="var(--card-dark)"/>
      <path d="M0 102 L340 102 Q350 102 356 110 L368 136 Q372 140 380 140 L520 140 L520 102 L520 100 L0 100 Z" fill="var(--accent)"/>
      <path d="M340 102 L520 102" stroke="var(--accent)" stroke-width="4"/>
      <rect x="0" y="102" width="340" height="4" fill="var(--accent)"/>
    </svg>

    <div class="brand">
      <span class="brand-dot"></span>
      <span class="brand-name">The Ember Vale</span>
    </div>

    <div class="holder">
      <div class="holder-name">Daniel Hale</div>
      <div class="holder-role">Director</div>
    </div>

    <ul class="contact-list">
      <li>
        <span class="icon">
          <svg width="8" height="8" viewBox="0 0 10 10"><path d="M2 1 L4 1 L4.6 3 L3.4 4 Q4.5 6 6 6.6 L7 5.4 L9 6 L9 8 Q9 9 8 9 Q1 8.5 1 2 Q1 1 2 1Z" fill="var(--accent)"/></svg>
        </span>+1 555 014 2281
      </li>
      <li>
        <span class="icon">
          <svg width="8" height="8" viewBox="0 0 10 10"><rect x="1" y="2.5" width="8" height="5.5" fill="none" stroke="var(--accent)" stroke-width="1.2"/><path d="M1 2.5 L5 5.5 L9 2.5" fill="none" stroke="var(--accent)" stroke-width="1.2"/></svg>
        </span>hello@embervale.example
      </li>
      <li>
        <span class="icon">
          <svg width="8" height="8" viewBox="0 0 10 10"><circle cx="5" cy="5" r="2" fill="var(--accent)"/></svg>
        </span>social.example/@EmberVale
      </li>
      <li>
        <span class="icon">
          <svg width="8" height="8" viewBox="0 0 10 10"><circle cx="5" cy="5" r="3.6" fill="none" stroke="var(--accent)" stroke-width="1.2"/><path d="M1.4 5 H8.6" stroke="var(--accent)" stroke-width="1"/></svg>
        </span><span>www.<span class="web-accent">embervale</span>.example</span>
      </li>
    </ul>

    <div class="address">
      <span class="icon">
        <svg width="8" height="8" viewBox="0 0 10 10"><path d="M5 9.5 L2 5 A3.2 3.2 0 1 1 8 5 Z" fill="var(--text-dark)"/></svg>
      </span>
      <p>42 Harbor Loop Suite K<br>Cedar Point, FL 30021</p>
    </div>
  </section>

</body>
</html>
```